vascular clinic webdesign (wordpress+neve theme+ elementor)

Create a nice webdesign for an existing website of a vascular surgery clinic. Vascular surgery is the medical specialty that treats arteries and veins. Content should not change. First landing page we can recreate content if needed, but internal pages should not change content. We currently use Neve theme (https://plumecraft.net/skins/orla/) in a Wordpress CMS, which is highly customizable, we prefer to keep using it, as it is standard in all our sites, and will be often upgraded. We also have Elementor Pro. Please visit current domain: lumeria.net.
Page is in portuguese. But you can do anything in English that I translate later, or you can use original domain content already in portuguese.
Selected design need to be coded in wordpress+neve+elementor

Minimum pages:
First Page/Landing page (https://lumeria.net/)
Contact page (https://lumeria.net/contato/)
Post/Article page
About us (https://lumeria.net/a-clinica/)
Posts Archive (https://lumeria.net/todos-artigos/)
The team (https://lumeria.net/sobre-nos-equipe-de-cirurgia-vascular-endovascular-ecografia-angiologia/)

Target Market(s)

mostly (70%) woman, 30 to 60 years

Industry/Entity Type

Health

Coding

Coded - Design and coding required

Number of Pages Required

5+ page

Font styles to use
Serif

Requirements
Should not have
• Will not change Wordpress for any other CMS
Prefer not to change theme Neve (https://plumecraft.net/skins/orla/)

```html
<!DOCTYPE html>
<html lang="en">
<head>
<meta charset="utf-8">
<title>Lumeria – Vascular Surgery Clinic</title>
<link href="https://fonts.googleapis.com/css2?family=Open+Sans:wght@400;600;700&family=Montserrat:wght@500;600;700&family=Oswald:wght@300;400;500&family=Titillium+Web:wght@400;600&display=swap" rel="stylesheet">
<style>
:root{
  --navy:#0b5383;
  --navy-dark:#08446c;
  --sky:#45aeea;
  --btn:#1177cc;
  --icon:#5b9bd5;
  --ink:#333;
  --muted:#555;
  --brick:#8b2c22;
  --footer:#3a3535;
  --white:#fff;
}
*{margin:0;padding:0;box-sizing:border-box}
html,body{width:1200px;height:3532px;overflow:hidden}
body{position:relative;font-family:"Open Sans",sans-serif;color:var(--ink);background:var(--white)}
.abs{position:absolute}
a{color:inherit;text-decoration:none}

.topbar{left:0;top:0;width:1200px;height:35px;background:var(--navy);color:var(--white);font-size:14px}
.topbar .info{left:80px;top:8px;display:flex;gap:12px;align-items:center}
.topbar .info span{display:flex;align-items:center;gap:5px}
.topbar .social{left:913px;top:7px;display:flex;gap:8px}
.topbar .social i{width:21px;height:21px;background:var(--white);border-radius:3px;display:block}
.topbar .login{left:1010px;top:8px;border-left:1px solid rgba(255,255,255,.5);padding-left:14px}

.header{left:0;top:35px;width:1200px;height:116px;background:var(--white)}
.brand{left:82px;top:30px;display:flex;align-items:center;gap:12px;font-family:"Open Sans",sans-serif;font-weight:600;font-size:44px;color:#1e2a44;letter-spacing:1px}
.brand i{width:22px;height:22px;background:var(--navy);display:block}
.nav{top:52px;font-family:"Open Sans",sans-serif;font-weight:700;font-size:15px;color:#1d1d1d}

.hero{left:0;top:151px;width:1200px;height:596px;background:linear-gradient(160deg,#b8b9a9 0%,#8f9b7e 20%,#b77b59 38%,#6f8a55 55%,#a9a79d 72%,#c8c8c4 100%)}
.hero-kicker{left:80px;top:330px;height:36px;padding:0 12px;background:var(--navy);color:#fff;font-family:"Titillium Web",sans-serif;font-size:25px;line-height:36px;opacity:.92}
.hero-title{left:80px;top:370px;height:50px;padding:0 12px;background:var(--brick);color:#fff;font-family:"Titillium Web",sans-serif;font-weight:600;font-size:36px;line-height:50px;opacity:.92}
.hero-btn{left:80px;top:441px;width:185px;height:42px;background:var(--navy);color:#fff;font-size:14px;font-weight:600;text-align:center;line-height:42px}

.about{left:0;top:727px;width:1200px;height:267px;background:var(--navy);color:#fff;text-align:center}
.wave{left:0;top:640px;width:1200px;height:110px}
.sec-title{font-family:"Montserrat",sans-serif;font-weight:600;letter-spacing:2px}
.about h2{position:absolute;left:0;width:1200px;top:15px;font-size:37px}
.about .rule{position:absolute;left:537px;top:77px;width:126px;height:1px;background:rgba(255,255,255,.7)}
.about p{position:absolute;left:95px;width:1010px;top:101px;font-size:16.5px;line-height:23px}
.about .btn-out{position:absolute;left:537px;top:209px;width:125px;height:34px;border:1px solid #fff;font-size:16px;line-height:32px}

.solutions-title{left:0;width:1200px;top:1022px;text-align:center;font-size:38px;color:#3a3a3a}
.solutions-rule{left:527px;top:1093px;width:146px;height:1px;background:#999}
.sol{width:240px;text-align:center}
.sol .ring{width:152px;height:152px;margin:0 auto;border-radius:50%;background:var(--icon);border:3px solid #1d3a66;display:flex;align-items:center;justify-content:center}
.sol h3{margin-top:20px;font-family:"Montserrat",sans-serif;font-weight:500;font-size:17px;letter-spacing:1.5px;color:#222}
.sol p{margin:18px auto 0;width:210px;font-family:Arial,sans-serif;font-size:13px;line-height:21.5px;color:#444}
.sol .btn{display:inline-block;margin-top:30px;width:104px;height:33px;background:var(--btn);color:#fff;font-family:Arial,sans-serif;font-size:14px;line-height:33px}

.story{left:0;top:1586px;width:600px;height:512px;background:linear-gradient(120deg,var(--navy) 0%,var(--navy-dark) 100%);color:#fff}
.story-photo{left:601px;top:1586px;width:599px;height:512px;background:linear-gradient(180deg,#7fb4e0 0%,#a9cbe6 22%,#c7463a 42%,#d9d3cb 58%,#707a74 78%,#4a5048 100%)}
.story .kick{position:absolute;left:89px;top:50px;font-size:12px;font-weight:600}
.story h2{position:absolute;left:89px;top:64px;font-family:"Montserrat",sans-serif;font-weight:700;font-size:22px;letter-spacing:.5px}
.story .lead{position:absolute;left:89px;top:103px;width:350px;font-family:Arial,sans-serif;font-size:18px;line-height:23px}
.story .body{position:absolute;left:89px;top:193px;width:410px;font-family:"Montserrat",sans-serif;font-size:14.5px;line-height:27px}
.story .btn{position:absolute;left:90px;top:360px;width:114px;height:39px;border:1px solid #fff;background:var(--btn);font-family:Arial,sans-serif;font-size:14px;text-align:center;line-height:37px}
.story-notch{left:546px;top:2027px;width:110px;height:80px}

.best{left:82px;top:2170px;width:354px;height:225px;border-left:3px solid var(--btn);padding-left:36px}
.best h3{margin-top:22px;font-family:"Oswald",sans-serif;font-weight:300;font-size:31px;color:#333}
.best h4{margin-top:2px;font-family:"Montserrat",sans-serif;font-weight:700;font-size:21px;color:var(--btn);letter-spacing:.5px}
.best p{margin-top:12px;font-size:12.5px;line-height:22px;color:#666}
.best .more{margin-top:16px;font-size:12.5px;color:var(--btn);font-weight:600}
.divider{left:436px;top:2170px;width:1px;height:225px;background:#ddd}
.benefits{left:481px;top:2184px}
.benefits h3{font-family:"Oswald",sans-serif;font-weight:400;font-size:20px;color:#4a6d8c}
.benefits ul{list-style:none;margin-top:16px}
.benefits li{display:flex;align-items:center;gap:12px;font-size:13px;color:#555;height:29.3px}
.video{left:803px;top:2170px;width:314px;height:185px;background:linear-gradient(120deg,#cfd6d8 0%,#eef0f0 40%,#bfc9cc 100%);border:1px solid #ccc}

.appt{left:67px;top:2543px;width:1067px;height:106px;background:var(--sky);color:#fff}
.doctor{left:89px;top:2454px;width:171px;height:195px;background:linear-gradient(180deg,#dde9f3 0%,#8cc1e6 55%,#5aa4d6 100%);border-radius:80px 80px 0 0}
.appt h3{position:absolute;left:204px;top:28px;font-family:"Oswald",sans-serif;font-weight:500;font-size:21px}
.appt small{position:absolute;left:204px;top:59px;font-size:12.5px}
.appt .btn{position:absolute;left:480px;top:29px;width:151px;height:37px;background:#fff;color:var(--sky);font-size:13px;text-align:center;line-height:37px}
.appt .call{position:absolute;left:724px;top:26px;font-size:10px}
.appt .num{position:absolute;left:729px;top:40px;font-size:27px;letter-spacing:1px}

.testi h2{position:absolute;left:0;width:1200px;top:2675px;text-align:center;font-family:"Montserrat",sans-serif;font-weight:600;font-size:31px;letter-spacing:2px;color:#444}
.testi p{position:absolute;left:108px;width:984px;top:2733px;text-align:center;font-size:13.5px;line-height:19.5px;color:#555}
.avatar{left:566px;top:2824px;width:82px;height:82px;border-radius:50%;background:linear-gradient(180deg,#e6e6e6,#b9c2cb);border:3px solid #eee}
.testi .name{position:absolute;left:0;width:1214px;top:2919px;text-align:center;font-size:14px;color:#555}
.testi .role{position:absolute;left:0;width:1214px;top:2941px;text-align:center;font-size:10px;color:#777}
.dots{left:571px;top:2973px;display:flex;gap:5px}
.dots i{width:22px;height:3px;background:#333;display:block}
.dots i.on{background:var(--btn)}

.footer{left:0;top:3033px;width:1200px;height:499px;background:var(--footer);color:#fff}
.footer h2{position:absolute;top:57px;font-family:"Montserrat",sans-serif;font-weight:600;font-size:26px}
.field{position:absolute;left:80px;width:290px;height:32px;background:#fff;color:#999;font-size:13px;padding:6px 6px}
.submit{position:absolute;left:80px;top:334px;width:117px;height:40px;background:var(--navy);font-family:"Titillium Web",sans-serif;font-size:17px;text-align:center;line-height:40px}
.label{position:absolute;top:138px;font-size:13.5px;letter-spacing:.5px}
.addr{position:absolute;left:443px;top:164px;font-family:"Montserrat",sans-serif;font-size:13px;line-height:18px}
.addr .row{display:flex;gap:12px;margin-bottom:14px}
.addr svg{flex:none}
.sol-list{position:absolute;left:706px;top:165px;list-style:none;font-family:"Montserrat",sans-serif;font-size:14px}
.sol-list li{height:26.6px;display:flex;align-items:center;gap:8px}
.sol-list li::before{content:"";width:7px;height:7px;border-radius:50%;background:#fff}
.badge-a{left:1005px;top:3177px;width:80px;height:70px;border-radius:50%;background:#e3a21a;border:4px solid #f5c84a}
.badge-b{left:1009px;top:3263px;width:68px;height:82px;background:#2c5aa0;border-radius:6px 6px 34px 34px}
.copy{position:absolute;left:0;width:1200px;top:438px;text-align:center;font-family:"Montserrat",sans-serif;font-size:13.5px}
</style>
</head>
<body>

<div class="topbar abs">
  <div class="info abs">
    <span><svg width="13" height="11" viewBox="0 0 13 11"><rect x=".5" y=".5" width="12" height="10" fill="none" stroke="#fff"/><path d="M1 1l5.5 5 5.5-5" fill="none" stroke="#fff"/></svg>contato@ondina.clinic</span>
    <span><svg width="13" height="13" viewBox="0 0 24 24"><path d="M6.6 10.8a15 15 0 006.6 6.6l2.2-2.2a1 1 0 011-.25 11.4 11.4 0 003.6.6 1 1 0 011 1V20a1 1 0 01-1 1A17 17 0 013 4a1 1 0 011-1h3.5a1 1 0 011 1 11.4 11.4 0 00.6 3.6 1 1 0 01-.25 1z" fill="#fff"/></svg>(011) 4870-3316</span>
    <span><svg width="11" height="14" viewBox="0 0 12 16"><path d="M6 0a6 6 0 00-6 6c0 4.5 6 10 6 10s6-5.5 6-10a6 6 0 00-6-6zm0 8.5A2.5 2.5 0 116 3.5a2.5 2.5 0 010 5z" fill="#fff"/></svg>Av. Aurora 1180, Campo Verde, CV</span>
  </div>
  <div class="social abs"><i></i><i></i><i></i></div>
  <div class="login abs">⇥ Client Login</div>
</div>

<header class="header abs">
  <a class="brand abs" href="https://lumeria.net/"><i></i>Lumeria</a>
  <a class="nav abs" style="left:521px" href="https://lumeria.net/a-clinica/">The Clinic</a>
  <a class="nav abs" style="left:639px" href="https://lumeria.net/sobre-nos-equipe-de-cirurgia-vascular-endovascular-ecografia-angiologia/">The team</a>
  <a class="nav abs" style="left:758px" href="https://lumeria.net/todos-artigos/">Vascular Problems</a>
  <a class="nav abs" style="left:943px">Solutions</a>
  <a class="nav abs" style="left:1058px" href="https://lumeria.net/contato/">Contact</a>
</header>

<section class="hero abs" role="img" aria-label="Aerial photograph of the clinic building among tree-lined city streets"></section>
<div class="hero-kicker abs">The Best Hospitality Clinic</div>
<div class="hero-title abs">We Care for your health</div>
<a class="hero-btn abs">BOOK APPOINTMENT</a>

<section class="about abs">
  <h2 class="sec-title">ABOUT CLINIC</h2>
  <div class="rule"></div>
  <p>Lumeria reiterates the pledge to help all and give hope to those who have lost hope. In this endeavor, while we have the best of an expert team of doctors taking care of the patients at one hand; we have an exemplary team of voluntary physicians and re-tired physicians who provide medical assistance to the not so wealthy class from negligible to no cost. No matter, what the story or situation is; Trust us to be there to help all and make things well again.</p>
  <a class="btn-out" href="https://lumeria.net/a-clinica/">Read More</a>
</section>
<svg class="wave abs" viewBox="0 0 1200 110" preserveAspectRatio="none">
  <path d="M0 20 Q600 150 1200 20 V110 H0Z" fill="#dcebf6"/>
  <path d="M0 40 Q600 150 1200 40 V110 H0Z" fill="#0b5383"/>
  <path d="M0 96 Q180 90 360 98" stroke="#fff" stroke-width="3" fill="none"/>
  <path d="M840 98 Q1020 90 1200 88" stroke="#fff" stroke-width="3" fill="none"/>
</svg>

<h2 class="solutions-title abs sec-title">SOLUTIONS</h2>
<div class="solutions-rule abs"></div>

<div class="sol abs" style="left:65px;top:1136px">
  <div class="ring"><svg width="62" height="56" viewBox="0 0 62 56"><path d="M31 52 C10 36 4 26 4 17 A13 13 0 0131 11 A13 13 0 0158 17 C58 26 52 36 31 52Z" fill="none" stroke="#fff" stroke-width="4"/><path d="M10 28h12l4-8 6 14 4-6h16" fill="none" stroke="#fff" stroke-width="3"/></svg></div>
  <h3>ARTERIALS</h3>
  <p>These FREE lab interpretation reports add value to your practice by providing you and your patients with easy-to-read reports that rank imbalances,</p>
  <a class="btn">Read More</a>
</div>
<div class="sol abs" style="left:339px;top:1136px">
  <div class="ring"><svg width="72" height="72" viewBox="0 0 72 72"><circle cx="36" cy="36" r="34" fill="#fff"/><path d="M20 40 V34 a16 16 0 0132 0 V40" fill="none" stroke="#5b9bd5" stroke-width="4"/><rect x="16" y="36" width="8" height="12" rx="3" fill="#5b9bd5"/><rect x="48" y="36" width="8" height="12" rx="3" fill="#5b9bd5"/></svg></div>
  <h3>VENOUS</h3>
  <p>These FREE lab interpretation reports add value to your practice by providing you and your patients with easy-to-read reports that rank imbalances,</p>
  <a class="btn">Read More</a>
</div>
<div class="sol abs" style="left:615px;top:1136px">
  <div class="ring"><svg width="50" height="64" viewBox="0 0 50 64"><path d="M25 2 C25 2 2 30 2 42 a23 23 0 0046 0 C48 30 25 2 25 2Z" fill="#fff"/><path d="M25 33v18M16 42h18" stroke="#5b9bd5" stroke-width="5"/></svg></div>
  <h3>LYMPHATICS</h3>
  <p>These FREE lab interpretation reports add value to your practice by providing you and your patients with easy-to-read reports that rank imbalances,</p>
  <a class="btn">Read More</a>
</div>
<div class="sol abs" style="left:888px;top:1136px">
  <div class="ring"><svg width="52" height="66" viewBox="0 0 52 66"><rect x="4" y="8" width="44" height="56" rx="4" fill="#fff"/><rect x="16" y="2" width="20" height="12" rx="3" fill="#fff" stroke="#5b9bd5" stroke-width="2"/><path d="M26 26v22M15 37h22" stroke="#5b9bd5" stroke-width="5"/></svg></div>
  <h3>VASCULAR EXAMINATIONS</h3>
  <p>These FREE lab interpretation reports add value to your practice by providing you and your patients with easy-to-read reports that rank imbalances,</p>
  <a class="btn">Read More</a>
</div>

<section class="story abs">
  <div class="kick">OUR STORY</div>
  <h2>YOU'RE IN GOOD HANDS</h2>
  <div class="lead">Great one let abundantly sixth let were one earth were him after tree seed over.</div>
  <div class="body">Second dominion saying one void beast. Called appear multiply light that. Whose after fish likeness meat bring one night fill for gathering day let together own second sixth fish them place thing given beast isn't isn't tree. Have.</div>
  <a class="btn">Know More</a>
</section>
<div class="story-photo abs" role="img" aria-label="Photograph of the clinic's red and white building facade behind a fence"></div>
<svg class="story-notch abs" viewBox="0 0 110 80"><path d="M0 30 L55 0 L110 30 V80 H0Z" fill="#fff"/></svg>

<div class="best abs">
  <h3>BEST IN CITY</h3>
  <h4>RADIOLOGY CENTER</h4>
  <p>Day is sea midst one female to under. It firmament she'd day had you may land can't signs likeness.</p>
  <div class="more">✚ KNOW MORE</div>
</div>
<div class="divider abs"></div>
<div class="benefits abs">
  <h3>QUICK LOOK AT BENEFITS</h3>
  <ul>
    <li><svg width="12" height="10" viewBox="0 0 12 10"><path d="M1 5l3.5 3.5L11 1.5" fill="none" stroke="#4a6d8c" stroke-width="2.2"/></svg>Qualified Staff of Doctors</li>
    <li><svg width="12" height="10" viewBox="0 0 12 10"><path d="M1 5l3.5 3.5L11 1.5" fill="none" stroke="#4a6d8c" stroke-width="2.2"/></svg>Feel like you are at Home Services</li>
    <li><svg width="12" height="10" viewBox="0 0 12 10"><path d="M1 5l3.5 3.5L11 1.5" fill="none" stroke="#4a6d8c" stroke-width="2.2"/></svg>24x7 Emergency Services</li>
    <li><svg width="12" height="10" viewBox="0 0 12 10"><path d="M1 5l3.5 3.5L11 1.5" fill="none" stroke="#4a6d8c" stroke-width="2.2"/></svg>Save your Money and Time with us</li>
    <li><svg width="12" height="10" viewBox="0 0 12 10"><path d="M1 5l3.5 3.5L11 1.5" fill="none" stroke="#4a6d8c" stroke-width="2.2"/></svg>Easy and Affordable Billing</li>
  </ul>
</div>
<div class="video abs" role="img" aria-label="Video still of the medical team beside a scanner">
  <svg style="position:absolute;left:136px;top:72px" width="40" height="40" viewBox="0 0 40 40"><circle cx="20" cy="20" r="19" fill="rgba(255,255,255,.8)"/><path d="M16 12l12 8-12 8z" fill="#9aa"/></svg>
</div>

<section class="appt abs">
  <h3>BOOK YOUR APPOINTMENT</h3>
  <small>It's easy and fast. Start now!</small>
  <a class="btn">BOOK NOW</a>
  <svg style="position:absolute;left:690px;top:28px" width="24" height="44" viewBox="0 0 24 44"><rect x="2" y="2" width="20" height="40" rx="4" fill="none" stroke="#fff" stroke-width="3"/><circle cx="12" cy="36" r="2" fill="#fff"/></svg>
  <div class="call">BOOK THROUGH CALL</div>
  <div class="num">(888) 555-0147</div>
</section>
<div class="doctor abs" role="img" aria-label="Smiling surgeon in scrubs and cap"></div>

<section class="testi">
  <h2>WHAT OUR PATIENTS SAY ABOUT US</h2>
  <p>Lorem Ipsum has been the industry's standard dummy text ever since the 1500s, when an unknown printer took a galley of type and scrambled it to make a type specimen book. It has survived not only five centuries, but also the leap into electronic typesetting, remaining essentially unchanged. It was popularised in the 1960s with the release of Ledgerline sheets containing Lorem Ipsum passages, and more recently with desktop publishing software like Folio Layout including versions</p>
  <div class="avatar abs" role="img" aria-label="Patient portrait"></div>
  <div class="name">TOMAS REYNE</div>
  <div class="role">HEART PATIENT</div>
  <div class="dots abs"><i></i><i class="on"></i><i></i></div>
</section>

<footer class="footer abs">
  <h2 style="left:82px">CONTACT US</h2>
  <div class="field" style="top:101px">Your Name</div>
  <div class="field" style="top:142px">Your Email</div>
  <div class="field" style="top:185px">Your Address</div>
  <div class="field" style="top:227px;height:81px">Your comments</div>
  <a class="submit">SUBMIT</a>

  <h2 style="left:443px">SOME DISEASES WE TREAT</h2>
  <div class="label" style="left:443px">ADDRESS</div>
  <div class="addr">
    <div class="row"><svg width="14" height="20" viewBox="0 0 12 16"><path d="M6 0a6 6 0 00-6 6c0 4.5 6 10 6 10s6-5.5 6-10a6 6 0 00-6-6zm0 8.5A2.5 2.5 0 116 3.5a2.5 2.5 0 010 5z" fill="#fff"/></svg><div>Av Aurora, 1180, Campo Verde, CV,<br>CEP 04512-090, Brasil.<br>Abra no mapa</div></div>
    <div class="row"><svg width="16" height="16" viewBox="0 0 16 16"><circle cx="8" cy="8" r="7" fill="none" stroke="#fff" stroke-width="1.4"/><path d="M1 8h14M8 1c-3 4-3 10 0 14M8 1c3 4 3 10 0 14" fill="none" stroke="#fff" stroke-width="1.2"/></svg><div>brisadiagnostics.net</div></div>
    <div class="row"><svg width="16" height="16" viewBox="0 0 24 24"><path d="M6.6 10.8a15 15 0 006.6 6.6l2.2-2.2a1 1 0 011-.25 11.4 11.4 0 003.6.6 1 1 0 011 1V20a1 1 0 01-1 1A17 17 0 013 4a1 1 0 011-1h3.5a1 1 0 011 1 11.4 11.4 0 00.6 3.6 1 1 0 01-.25 1z" fill="#fff"/></svg><div>(888) 555-0147</div></div>
    <div class="row"><svg width="18" height="13" viewBox="0 0 13 11"><rect x=".5" y=".5" width="12" height="10" fill="none" stroke="#fff"/><path d="M1 1l5.5 5 5.5-5" fill="none" stroke="#fff"/></svg><div>info@brisadiagnostics.net</div></div>
  </div>
  <div class="label" style="left:706px">SOLUTIONS</div>
  <ul class="sol-list">
    <li>About Us</li>
    <li>Northfield Hospital</li>
    <li>Hospital Santa Clara Vale</li>
    <li>Ondina Institute</li>
    <li>About Medical Reimbursement</li>
    <li></li>
  </ul>
  <div class="copy">Copyright © 2020. Your trusted Vascular Surgery medical team in Campo Verde, CV.</div>
</footer>
<div class="badge-a abs" role="img" aria-label="Rating badge"></div>
<div class="badge-b abs" role="img" aria-label="Review rating badge"></div>

</body>
</html>
```